Brava Set CEO and Partners Business Card

We need a fresh, fun, simple and clean business card design....we would like a template where we can add a name and title (as well as specific email addresses). We are open to different looks (full logo on one side and a small logo on the company info side, or our logo is in the background but faint on one side but full on the other, or something else cool :-) ). Our colors are in our logo: blue, black and white...however we are not opposed to the use of other colors if it works. We build sets, make props and a host of other things for the film and television industry...our card should reflect creativity, style and professionalism.

A white background would be preferred.

I would like to see an option with Facebook and Instagram icons.

Facebook- facebook.com/bravasetny
Instagram- brava_set

Our website is bravaset-example.com.

Brava Set, Inc.
418 Corvell Avenue, Unit 9
North Hollywood, California 91602
555.210.4873 | tel
555.210.6692 | fax
www.BravaSet-example.com

Sample Name and Title #1:

Peter Halvik
CEO / Co-Owner
555.210.4873 | tel
555.210.6692 | fax
peter@bravaset-example.com
www.BravaSet-example.com

Target Market(s)

Marketing Professionals, Production Designers, Interior Designers, Film Producers, Directors, Art Directors, Event Directors

Industry/Entity Type

Entertainment Industry

Contact Information for Business Card

Peter Halvik
CEO / Co-Owner
555.210.4873 | tel
555.210.6692 | fax
peter@bravaset-example.com
www.BravaSet-example.com

Font styles to use
Sans Serif

Colors
33a6d7
ffffff
1b1b1b

Requirements
Must have
• Logo, All Contact Info, White Background. Symmetry.
Nice to have
• Facebook and Instagram icons with addresses
• Facebook- facebook.com/bravasetny
• Instagram- brava_set

```html
<!DOCTYPE html>
<html lang="en">
<head>
<meta charset="utf-8">
<title>Brava Set — Business Card</title>
<link rel="stylesheet" href="https://fonts.googleapis.com/css2?family=Open+Sans:wght@400;700&family=Russo+One&display=swap">
<style>
  :root {
    --brand-blue: #33a6d7;
    --brand-black: #1b1b1b;
    --card-black: #0a0a0a;
    --paper: #ffffff;
    --backdrop: #e9eaec;
    --ink-soft: #2a2a2a;
  }
  * { box-sizing: border-box; margin: 0; padding: 0; }
  html, body { width: 799px; height: 1200px; overflow: hidden; }
  body {
    background: var(--backdrop);
    font-family: "Open Sans", Arial, sans-serif;
    color: var(--brand-black);
    position: relative;
  }
  .card {
    position: absolute;
    left: 60px;
    width: 680px;
    height: 389px;
    background: var(--card-black);
    border-radius: 6px;
    overflow: hidden;
    box-shadow: 0 10px 24px rgba(0,0,0,0.18);
  }
  .card--front { top: 150px; }
  .card--back { top: 660px; }

  .front-panel {
    position: absolute;
    left: 70px; top: 40px;
    width: 380px; height: 309px;
    background: var(--paper);
    border-radius: 26px;
    display: flex; align-items: center; justify-content: center;
  }
  .wordmark {
    display: flex; align-items: center; gap: 12px;
    font-family: "Russo One", "Open Sans", sans-serif;
    color: var(--brand-black);
    letter-spacing: 1px;
    text-transform: uppercase;
  }
  .wordmark__dot { background: var(--brand-blue); border-radius: 4px; }
  .front-panel .wordmark { font-size: 52px; }
  .front-panel .wordmark__dot { width: 30px; height: 30px; }

  .back-panel {
    position: absolute;
    left: 30px; top: 30px;
    width: 560px; height: 329px;
    background: var(--paper);
    border-radius: 26px 0 0 26px;
  }
  .accent-arc { position: absolute; right: 0; top: 0; width: 680px; height: 389px; }
  .back-content { position: absolute; left: 64px; top: 58px; }
  .back-content .wordmark { font-size: 38px; }
  .back-content .wordmark__dot { width: 22px; height: 22px; }

  .person { margin-top: 24px; }
  .person__name { font-weight: 700; font-size: 19px; color: var(--brand-black); }
  .person__title { font-size: 14px; color: var(--brand-blue); margin-top: 1px; }

  .contact-list { list-style: none; margin-top: 12px; font-size: 13px; color: var(--ink-soft); line-height: 19px; }
  .contact-list li { display: flex; align-items: flex-start; gap: 9px; }
  .contact-list svg { width: 12px; height: 12px; margin-top: 3px; flex: none; fill: var(--brand-blue); }

  .social-list { list-style: none; margin-top: 12px; font-size: 13px; color: var(--ink-soft); line-height: 19px; }
  .social-list li { display: flex; align-items: center; gap: 9px; }
  .social-chip { width: 12px; height: 12px; border-radius: 2px; background: var(--brand-blue); flex: none; }
</style>
</head>
<body>

  <section class="card card--front" aria-label="Card front">
    <div class="front-panel">
      <div class="wordmark"><span class="wordmark__dot"></span><span>Brava Set</span></div>
    </div>
  </section>

  <section class="card card--back" aria-label="Card back">
    <div class="back-panel"></div>
    <svg class="accent-arc" viewBox="0 0 680 389" aria-hidden="true">
      <path d="M590 30 A230 230 0 0 1 680 250 L680 359 L590 359 Z" fill="#ffffff"/>
      <path d="M600 30 C660 100 680 180 680 230 L680 30 Z" fill="var(--brand-blue)"/>
      <path d="M590 30 L600 30 C660 100 680 180 680 230 L680 389 L590 389 Z" fill="none"/>
    </svg>

    <div class="back-content">
      <div class="wordmark"><span class="wordmark__dot"></span><span>Brava Set</span></div>

      <div class="person">
        <div class="person__name">Peter Halvik</div>
        <div class="person__title">CEO / Co-Owner</div>
      </div>

      <ul class="contact-list">
        <li><svg viewBox="0 0 12 12"><path d="M2.5 0.5l2 2.5-1.2 1.4c.7 1.5 1.8 2.6 3.3 3.3L8 6.5l2.5 2-1.2 2.8C5 11 1 7 .7 2.6z"/></svg>555.210.4873</li>
        <li><svg viewBox="0 0 12 12"><rect x="3" y="0.5" width="6" height="3.5"/><rect x="0.5" y="4.5" width="11" height="5" rx="1"/><rect x="3" y="8" width="6" height="3.5"/></svg>555.210.6692</li>
        <li><svg viewBox="0 0 12 12"><path d="M0.5 2h11v8h-11z M1 2.5l5 4 5-4" stroke="#fff" stroke-width="0.8"/></svg>peter@bravaset-example.com</li>
        <li><svg viewBox="0 0 12 12"><circle cx="6" cy="6" r="5.5"/><path d="M0.5 6h11M6 0.5c-2.5 3-2.5 8 0 11M6 0.5c2.5 3 2.5 8 0 11" stroke="#fff" stroke-width="0.7" fill="none"/></svg>www.BravaSet-example.com</li>
        <li><svg viewBox="0 0 12 12"><path d="M6 0.5a4 4 0 0 1 4 4c0 3-4 7-4 7s-4-4-4-7a4 4 0 0 1 4-4z"/><circle cx="6" cy="4.5" r="1.5" fill="#fff"/></svg><span>418 Corvell Avenue, Unit 9<br>North Hollywood, California 91602</span></li>
      </ul>

      <ul class="social-list">
        <li><span class="social-chip"></span>bravasetny</li>
        <li><span class="social-chip"></span>brava_set</li>
      </ul>
    </div>
  </section>

</body>
</html>
```